Business card design needed for Automotive Reconditioning business

I have a logo design i just cant decide on the best color or layout for the business card, I will upload all the files so you can see all colors schemes we are considering. I have other file formats if needed let me know.

Target Market(s)

automotive dealerships

Contact Information for Business Card

HERE are the Descriptions and info needed on the card:
Interior Repair: Leather carpet burns panels dash Deoderize
Dealer products and Vin Verify
( spot for name and cell number) My name is Norman Bexley phone 614 352-4180 Title COO www.QuorvalMotive.com

Font styles to use
Sans Serif
Other font styles liked:
• what ever you think looks best

Requirements
Must have
• Must be able to change the name and phone for employees

```html
<!DOCTYPE html>
<html lang="en">
<head>
<meta charset="utf-8">
<title>Quorval Motive – Business Card</title>
<link href="https://fonts.googleapis.com/css2?family=Open+Sans:wght@400;600&family=Russo+One&display=swap" rel="stylesheet">
<style>
  :root {
    --page-bg: #2b2b2d;
    --card-dark: #3c3c3e;
    --photo-deep: #0d0d12;
    --photo-mid: #2a2836;
    --photo-silver: #9a9aa3;
    --accent-blue: #2a8fd6;
    --text-white: #ffffff;
    --text-soft: #e6e6e8;
  }
  * { margin: 0; padding: 0; box-sizing: border-box; }
  html, body {
    width: 1200px;
    height: 716px;
    overflow: hidden;
    background: var(--page-bg);
  }
  .canvas {
    position: relative;
    width: 1200px;
    height: 716px;
    display: flex;
    align-items: center;
    justify-content: center;
    gap: 60px;
  }
  .card {
    position: relative;
    width: 510px;
    height: 292px;
    border-radius: 4px;
    overflow: hidden;
    box-shadow: 0 10px 28px rgba(0,0,0,.45);
  }

  /* Back card */
  .card-back__photo {
    position: absolute;
    inset: 0;
    background:
      radial-gradient(ellipse 45% 70% at 72% 42%, var(--photo-silver) 0%, #5b5b66 35%, transparent 70%),
      linear-gradient(135deg, var(--photo-deep) 0%, var(--photo-mid) 60%, #1a1a24 100%);
  }
  .card-back__services {
    position: absolute;
    left: 14px;
    top: 122px;
    width: 420px;
    font-family: "Open Sans", sans-serif;
    font-size: 13.5px;
    line-height: 1.35;
    color: var(--text-white);
    text-align: center;
  }
  .card-back__services span {
    display: block;
    white-space: nowrap;
  }

  /* Front card */
  .card-front { background: var(--card-dark); }
  .card-front__art {
    position: absolute;
    inset: 0;
    width: 100%;
    height: 100%;
  }
  .card-front__photo {
    position: absolute;
    left: 0;
    top: 0;
    width: 220px;
    height: 292px;
  }
  .card-front__company {
    position: absolute;
    left: 262px;
    top: 80px;
    width: 238px;
    font-family: "Russo One", sans-serif;
    font-size: 15px;
    line-height: 1.25;
    color: var(--text-white);
    text-align: center;
    letter-spacing: .5px;
    white-space: nowrap;
  }
  .card-front__person {
    position: absolute;
    left: 262px;
    top: 146px;
    width: 238px;
    text-align: center;
    font-family: "Russo One", sans-serif;
  }
  .person__name {
    font-size: 16px;
    color: var(--text-white);
    letter-spacing: .5px;
  }
  .person__name .surname { color: var(--accent-blue); }
  .person__title {
    font-size: 12px;
    color: var(--text-white);
    margin-top: 2px;
  }
  .contact {
    position: absolute;
    left: 262px;
    top: 206px;
    width: 238px;
    text-align: center;
    font-family: "Open Sans", sans-serif;
    color: var(--text-soft);
  }
  .contact__icon { display: block; margin: 0 auto 6px; }
  .contact__phone { font-size: 13px; letter-spacing: 1px; }
  .contact__web { font-size: 12px; letter-spacing: .5px; margin-top: 6px; }
</style>
</head>
<body>
<main class="canvas">

  <section class="card card-back">
    <div class="card-back__photo" role="img" aria-label="Close-up photo of a silver sports car rear with red tail light on a dark background"></div>
    <p class="card-back__services">
      <span>Interior Repair: Leather carpet burns panels dash Deoderize</span>
      <span>Dealer products and Vin Verify</span>
    </p>
  </section>

  <section class="card card-front">
    <svg class="card-front__art" viewBox="0 0 510 292" aria-hidden="true">
      <defs>
        <radialGradient id="car-photo-tone" cx="40%" cy="55%" r="70%">
          <stop offset="0" stop-color="#3a3848"/>
          <stop offset=".55" stop-color="#17161e"/>
          <stop offset="1" stop-color="#07070a"/>
        </radialGradient>
      </defs>
      <path d="M0,0 H262 C214,80 198,180 206,292 H0 Z" fill="url(#car-photo-tone)"/>
      <path d="M262,0 H280 C236,82 226,186 250,292 H206 C198,180 214,80 262,0 Z" fill="var(--accent-blue)"/>
    </svg>
    <div class="card-front__photo" role="img" aria-label="Photo of a black sports car with orange wheels seen from the rear quarter"></div>

    <p class="card-front__company">QUORVAL MOTIVE<br>RECONDITIONING CORP</p>

    <div class="card-front__person">
      <p class="person__name">NORMAN <span class="surname">BEXLEY</span></p>
      <p class="person__title">COO</p>
    </div>

    <div class="contact">
      <svg class="contact__icon" width="12" height="14" viewBox="0 0 24 24" aria-hidden="true">
        <path fill="var(--accent-blue)" d="M6.6 10.8a15.1 15.1 0 0 0 6.6 6.6l2.2-2.2a1 1 0 0 1 1-.25 11.4 11.4 0 0 0 3.6.57 1 1 0 0 1 1 1V20a1 1 0 0 1-1 1A17 17 0 0 1 3 4a1 1 0 0 1 1-1h3.5a1 1 0 0 1 1 1c0 1.25.2 2.45.57 3.57a1 1 0 0 1-.25 1z"/>
      </svg>
      <p class="contact__phone">614 352-4180</p>
      <p class="contact__web">www.QuorvalMotive.com</p>
    </div>
  </section>

</main>
</body>
</html>
```